Corvena Card

The logo is the Spanish flag colors I want a vibrant eye catching design with the yellow / red colors over either Navy or white background or black even ,
Would like a 2D feel to the logo with another lighter color logo under it look ,

Contact Information for Business Card

Corvena Flooring
Tobin Reswick
Main Number
Cell Number
Fax Number

Website on the side of the card somewhere

Font styles to use
Sans Serif

Colors
ec1f27
ffc214

Requirements
Must have
• 2 logos feel one is bolder and the other one underneath very light

```html
<!DOCTYPE html>
<html lang="en">
<head>
<meta charset="utf-8">
<title>Corvena Flooring – Business Card</title>
<link href="https://fonts.googleapis.com/css2?family=Montserrat:wght@400;500;600;700&display=swap" rel="stylesheet">
<style>
  :root {
    --navy: #25234a;
    --navy-deep: #1d1c3d;
    --red: #ec1f27;
    --yellow: #ffc214;
    --silver: #c9c9d2;
    --white: #f2f2f6;
    --backdrop: #2b2b2e;
  }
  * { margin: 0; padding: 0; box-sizing: border-box; }
  html, body { width: 1200px; height: 900px; overflow: hidden; }
  body {
    background: var(--backdrop);
    font-family: "Montserrat", Arial, sans-serif;
    position: relative;
  }
  .card {
    position: absolute;
    left: 320px;
    width: 560px;
    height: 320px;
    border-radius: 26px;
    background: linear-gradient(135deg, var(--navy) 0%, var(--navy-deep) 100%);
    border: 4px solid var(--red);
    overflow: hidden;
  }
  .card-front { top: 90px; }
  .card-back { top: 470px; }

  /* Front */
  .front-brand {
    position: absolute;
    inset: 0;
    display: flex;
    flex-direction: column;
    align-items: center;
    justify-content: center;
    gap: 14px;
  }
  .front-mark {
    width: 70px; height: 70px;
    background: var(--silver);
  }
  .front-name {
    color: var(--silver);
    font-weight: 600;
    font-size: 40px;
    letter-spacing: 10px;
    margin-right: -10px;
  }
  .front-tag {
    color: var(--silver);
    font-weight: 500;
    font-size: 15px;
    letter-spacing: 9px;
    margin-top: -8px;
  }

  /* Back */
  .back-brand {
    position: absolute;
    left: 34px; top: 30px;
    display: flex; align-items: center; gap: 14px;
  }
  .back-mark { width: 46px; height: 46px; background: var(--yellow); }
  .back-name {
    color: var(--yellow);
    font-weight: 700;
    font-size: 28px;
    letter-spacing: 5px;
    line-height: 1;
  }
  .back-tag {
    color: var(--red);
    font-weight: 600;
    font-size: 11px;
    letter-spacing: 7px;
    margin-top: 6px;
  }
  .person { position: absolute; left: 34px; top: 104px; }
  .person-name {
    color: var(--red);
    font-weight: 700;
    font-size: 20px;
    letter-spacing: 2px;
    font-variant: small-caps;
  }
  .person-role { color: var(--white); font-size: 13px; margin-top: 2px; }
  .address {
    position: absolute; left: 34px; top: 160px;
    color: var(--white); font-size: 13px; line-height: 1.35;
  }
  .contact-list {
    position: absolute; left: 34px; top: 204px;
    list-style: none;
  }
  .contact-list li {
    display: flex; align-items: center; gap: 10px;
    color: var(--white); font-size: 13px; line-height: 19px;
  }
  .contact-list svg { width: 13px; height: 13px; fill: var(--red); flex: none; }
</style>
</head>
<body>

<section class="card card-front" aria-label="Card front">
  <div class="front-brand">
    <div class="front-mark"></div>
    <div class="front-name">CORVENA</div>
    <div class="front-tag">· FLOORING ·</div>
  </div>
</section>

<section class="card card-back" aria-label="Card back">
  <div class="back-brand">
    <div class="back-mark"></div>
    <div>
      <div class="back-name">CORVENA</div>
      <div class="back-tag">· FLOORING ·</div>
    </div>
  </div>

  <div class="person">
    <div class="person-name">Tobin Reswick</div>
    <div class="person-role">Owner</div>
  </div>

  <div class="address">Here is your full address<br>Road no.123, Texas, USA</div>

  <ul class="contact-list">
    <li><svg viewBox="0 0 16 16"><path d="M3 1h3l1.5 4-2 1.3a9 9 0 0 0 4.2 4.2L11 8.5l4 1.5v3a2 2 0 0 1-2 2A12 12 0 0 1 1 3a2 2 0 0 1 2-2z"/></svg>512-408-3170</li>
    <li><svg viewBox="0 0 16 16"><path d="M4 0h8a1 1 0 0 1 1 1v14a1 1 0 0 1-1 1H4a1 1 0 0 1-1-1V1a1 1 0 0 1 1-1zm1 2v10h6V2zm3 11a1 1 0 1 0 0 2 1 1 0 0 0 0-2z"/></svg>512-408-3170</li>
    <li><svg viewBox="0 0 16 16"><path d="M4 0h7v4H4zM1 5h14v8h-2v3H3v-3H1zm4 5v4h6v-4z"/></svg>512-408-3170</li>
    <li><svg viewBox="0 0 16 16"><path d="M0 3h16v1L8 9 0 4zm0 3l8 5 8-5v7H0z"/></svg>info@CorvenaFlooring.com</li>
    <li><svg viewBox="0 0 16 16"><path d="M8 0a8 8 0 1 0 0 16A8 8 0 0 0 8 0zm0 2a6 6 0 0 1 5.7 4H10V4H7v3H4v3h3v4A6 6 0 0 1 8 2z"/></svg>www.CorvenaFlooring.com</li>
  </ul>
</section>

</body>
</html>
```